Inspiration Poster

Inspirational Poster that has a Kamran Dulo like abstract look (http://www.vexalo.com/images/search?q=kamran+dulo&FORM=HDRSC2) with the text:

"we walk not in order to arrive at the promise land but because walking itself is a revolution"
-Peter Ambrick

```html
<!DOCTYPE html>
<html lang="en">
<head>
<meta charset="utf-8">
<title>Inspiration Poster – Walking Is a Revolution</title>
<link rel="stylesheet" href="https://fonts.googleapis.com/css2?family=Archivo+Black&family=Montserrat:wght@600&family=Arimo&display=swap">
<style>
  :root {
    --ink-deep: #0d1a2e;
    --red-glow: #e2321c;
    --orange-glow: #f06a2a;
    --sky-light: #bfe4f7;
    --violet-light: #b9a6e8;
    --blue-mid: #2e5aa8;
    --green-glow: #3c9a3a;
    --yellow-glow: #e6e23a;
    --shade-dark: rgba(16, 22, 40, 0.62);
    --tint-light: rgba(235, 245, 255, 0.22);
    --tint-sky: rgba(160, 215, 250, 0.38);
    --tint-green: rgba(170, 225, 70, 0.38);
    --type-white: #ffffff;
  }
  html, body {
    margin: 0;
    padding: 0;
    width: 849px;
    height: 1200px;
    overflow: hidden;
    background: var(--ink-deep);
  }
  .poster {
    position: relative;
    width: 849px;
    height: 1200px;
    overflow: hidden;
  }
  .light-field {
    position: absolute;
    inset: 0;
    background:
      radial-gradient(ellipse 260px 200px at 330px 330px, var(--red-glow), transparent 70%),
      radial-gradient(ellipse 200px 160px at 170px 560px, var(--orange-glow), transparent 70%),
      radial-gradient(ellipse 280px 220px at 720px 230px, var(--sky-light), transparent 70%),
      radial-gradient(ellipse 220px 140px at 540px 150px, var(--violet-light), transparent 70%),
      radial-gradient(ellipse 260px 160px at 190px 850px, #d7d2ee, transparent 70%),
      radial-gradient(ellipse 240px 200px at 720px 640px, var(--blue-mid), transparent 70%),
      radial-gradient(ellipse 280px 220px at 640px 960px, var(--yellow-glow), transparent 70%),
      radial-gradient(ellipse 380px 260px at 420px 1080px, var(--green-glow), transparent 72%),
      radial-gradient(ellipse 300px 240px at 120px 160px, #1f3a5a, transparent 75%),
      linear-gradient(160deg, #24405e 0%, #7a2a2a 40%, #3e4f7a 65%, #3b6b34 100%);
  }
  .facets {
    position: absolute;
    inset: 0;
  }
  .facet-shade { fill: var(--shade-dark); }
  .facet-light { fill: var(--tint-light); }
  .facet-sky { fill: var(--tint-sky); }
  .facet-green { fill: var(--tint-green); }
  .quote {
    position: absolute;
    left: 233px;
    top: 498px;
    margin: 0;
    color: var(--type-white);
    font-family: "Archivo Black", "Arial Black", sans-serif;
    font-size: 41px;
    line-height: 45.5px;
    letter-spacing: -0.3px;
  }
  .quote-line { display: block; white-space: nowrap; }
  .quote-keyword {
    font-family: "Montserrat", sans-serif;
    font-weight: 600;
    font-size: 40px;
    letter-spacing: 5px;
    text-transform: uppercase;
  }
  .quote-author {
    position: absolute;
    left: 546px;
    top: 790px;
    margin: 0;
    color: var(--type-white);
    font-family: "Arimo", Arial, sans-serif;
    font-size: 14px;
  }
</style>
</head>
<body>
  <main class="poster">
    <div class="light-field" role="img" aria-label="Abstract long-exposure light photograph with streaks of red, blue, violet, yellow and green"></div>
    <svg class="facets" width="849" height="1200" viewBox="0 0 849 1200" aria-hidden="true">
      <polygon class="facet-light" points="380,0 752,0 556,332"/>
      <polygon class="facet-sky" points="556,332 849,80 849,480"/>
      <polygon class="facet-shade" points="28,567 757,305 466,958"/>
      <polygon class="facet-green" points="358,958 652,688 849,985"/>
    </svg>
    <blockquote class="quote">
      <span class="quote-line">“we walk not in</span>
      <span class="quote-line">order to arrive at</span>
      <span class="quote-line">the promise land</span>
      <span class="quote-line">but because</span>
      <span class="quote-line">walking itself is a</span>
      <span class="quote-line"><span class="quote-keyword">Revolution</span>”</span>
    </blockquote>
    <p class="quote-author">Peter Ambrick</p>
  </main>
</body>
</html>
```